Design Bag for Kilo Crunch Snacks

Create a full front and back design for Kilo Crunch Snacks with area for nutrition label. I would like a to take Kilo Crunch Snacks into the 21st century with a Hawaiian vibe. I would like a window about 2 inches from bottom to see the jerky chip.
Must Haves:
Hawai'i's Premium Beef Jerky Chips
100% Grass Fed Hawai'i Beef No Antibiotics No Growth Hormones
Made Exclusively In Hawaii
Extra Thin Extra Crispy

Target Market(s)

18-75 who doesnt like jerky

Requirements
Must have
• Hawai'i's Premium Beef Jerky Chips
Extra Thin, Extra Crispy
Color
Window
Area for the flavor. Start with TERIYAKI

```html
<!DOCTYPE html>
<html lang="en">
<head>
<meta charset="utf-8">
<title>Kilo Crunch Snacks – Beef Jerky Chips Pouch</title>
<link rel="stylesheet" href="https://fonts.googleapis.com/css2?family=Patua+One&family=Oswald:wght@500;600&family=Open+Sans:wght@700&display=swap">
<style>
  :root {
    --backdrop: #b3b3b3;
    --pouch-top: #e8707a;
    --pouch-mid: #cf3f4a;
    --pouch-low: #a8464a;
    --pouch-base: #8a3c3f;
    --window-a: #6f2a2c;
    --window-b: #a2484a;
    --headline-yellow: #f4ec1c;
    --headline-white: #ffffff;
    --ribbon-blue: #2a86d4;
    --ribbon-deep: #1a4f8f;
    --ribbon-tail: #1b2f4a;
    --badge-ring: #222222;
    --badge-red: #c8323b;
    --arc-text: #ffffff;
  }
  * { margin: 0; padding: 0; box-sizing: border-box; }
  html, body {
    width: 1200px;
    height: 888px;
    overflow: hidden;
    background: var(--backdrop);
  }
  .pouch {
    position: absolute;
    left: 385px;
    top: 96px;
    width: 430px;
    height: 738px;
  }
  .pouch svg { display: block; }
  .headline-premium {
    font-family: "Patua One", Georgia, serif;
    font-size: 27px;
    fill: var(--headline-yellow);
  }
  .headline-product {
    font-family: "Patua One", Georgia, serif;
    font-size: 37px;
    fill: var(--headline-white);
  }
  .arc-copy {
    font-family: "Open Sans", Arial, sans-serif;
    font-weight: 700;
    font-size: 12.5px;
    fill: var(--arc-text);
    letter-spacing: 0.5px;
  }
  .brand-name {
    font-family: "Patua One", Georgia, serif;
    font-size: 31px;
    fill: var(--badge-red);
  }
  .ribbon-copy {
    font-family: "Oswald", "Arial Narrow", sans-serif;
    font-weight: 600;
    font-size: 25px;
    fill: var(--headline-white);
  }
  .claims-copy {
    font-family: "Oswald", "Arial Narrow", sans-serif;
    font-weight: 500;
    font-size: 21px;
    fill: var(--headline-yellow);
  }
</style>
</head>
<body>
  <div class="pouch">
    <svg width="430" height="738" viewBox="0 0 430 738">
      <defs>
        <linearGradient id="pouch-fill" x1="0" y1="0" x2="0" y2="1">
          <stop offset="0" stop-color="var(--pouch-top)"/>
          <stop offset="0.45" stop-color="var(--pouch-mid)"/>
          <stop offset="0.75" stop-color="var(--pouch-low)"/>
          <stop offset="1" stop-color="var(--pouch-base)"/>
        </linearGradient>
        <linearGradient id="window-fill" x1="0" y1="0" x2="1" y2="1">
          <stop offset="0" stop-color="var(--window-b)"/>
          <stop offset="0.5" stop-color="var(--window-a)"/>
          <stop offset="1" stop-color="var(--window-b)"/>
        </linearGradient>
        <linearGradient id="ribbon-fill" x1="0" y1="0" x2="1" y2="0">
          <stop offset="0" stop-color="var(--ribbon-blue)"/>
          <stop offset="0.5" stop-color="var(--ribbon-deep)"/>
          <stop offset="1" stop-color="var(--ribbon-blue)"/>
        </linearGradient>
        <path id="arc-left" d="M 112.8 393 A 118 118 0 0 1 215 216"/>
        <path id="arc-right" d="M 255.4 223.1 A 118 118 0 0 1 274 436.2"/>
      </defs>

      <!-- pouch body with tropical backdrop -->
      <path class="pouch-body" role="img" aria-label="Tropical hibiscus flower and palm leaf pattern"
            d="M0 0 H430 V62 a6 6 0 0 0 0 12 V738 H0 V74 a6 6 0 0 0 0 -12 Z"
            fill="url(#pouch-fill)"/>
      <line class="zip-seam" x1="28" y1="120" x2="402" y2="120" stroke="#ffffff" stroke-opacity="0.12" stroke-width="2"/>

      <!-- headline -->
      <text class="headline-premium" x="215" y="147" text-anchor="middle">HAWAI'I'S PREMIUM</text>
      <text class="headline-product" x="215" y="186" text-anchor="middle">BEEF JERKY CHIPS</text>

      <!-- brand circle -->
      <text class="arc-copy"><textPath href="#arc-left" startOffset="50%" text-anchor="middle">MADE EXCLUSIVELY IN HAWAII</textPath></text>
      <text class="arc-copy"><textPath href="#arc-right" startOffset="50%" text-anchor="middle">EXTRA THIN EXTRA CRISPY</textPath></text>
      <circle class="brand-circle" cx="215" cy="334" r="104" fill="#ffffff"/>
      <text class="brand-name" text-anchor="middle">
        <tspan x="215" y="306">Kilo</tspan>
        <tspan x="215" y="342">Crunch</tspan>
        <tspan x="215" y="378">Snacks</tspan>
      </text>

      <!-- ribbon -->
      <g class="ribbon" transform="rotate(-7 215 512)">
        <path d="M38 486 L90 490 L90 528 L48 530 L62 509 Z" fill="var(--ribbon-tail)"/>
        <path d="M392 486 L340 490 L340 528 L382 530 L368 509 Z" fill="var(--ribbon-tail)"/>
        <path d="M70 492 Q215 470 360 492 L360 532 Q215 512 70 532 Z" fill="url(#ribbon-fill)"/>
        <text class="ribbon-copy" x="215" y="519" text-anchor="middle" textLength="262" lengthAdjust="spacingAndGlyphs">100% GRASS FED HAWAI'I BEEF</text>
      </g>

      <!-- claims -->
      <text class="claims-copy" x="215" y="578" text-anchor="middle" textLength="292" lengthAdjust="spacingAndGlyphs">No Antibiotics No Growth Hormones</text>

      <!-- product window -->
      <rect class="product-window" role="img" aria-label="Clear window showing the beef jerky chips inside"
            x="56" y="588" width="318" height="150" fill="url(#window-fill)"/>
    </svg>
  </div>
</body>
</html>
```